Rack Card for Silver Reel productions

Looking to make a verticle rack card back and front 3.5 X 8.5, add .125 on each side for bleed, CMYK, need .psd file and all fonts. We are based out of Connecticut but we are adding a location in Florida so it needs to be beach themed. I have a sample photo image but something else could be used. Front side should have image, logo, back side should have pricing. For your reference our Connecticut site is www.srpvowfilms.com but the Florida site will be
www.srpcoast.com
555-372-6148

Target Market(s)

Brides

Industry/Entity Type

Wedding Photography

Requirements
Must have
• Beach theme

```html
<!DOCTYPE html>
<html lang="en">
<head>
<meta charset="utf-8">
<title>Silver Reel productions – Rack Card</title>
<link href="https://fonts.googleapis.com/css2?family=Crimson+Pro:wght@400&family=Lato:wght@300;400&display=swap" rel="stylesheet">
<style>
  :root{
    --stage:#d9d9d9;
    --paper:#ffffff;
    --ribbon:#3f93c9;
    --heading:#3a8cc4;
    --ink:#2b2b2b;
    --logo-ink:#1f1f1f;
    --sea-deep:#3f6f73;
    --sea-foam:#cfd9d6;
    --sand-light:#c9b39a;
    --sand-dark:#8f7660;
    --rule:#4b9ad0;
  }
  *{box-sizing:border-box;margin:0;padding:0}
  html,body{width:1200px;height:900px;overflow:hidden}
  body{background:var(--stage);position:relative;font-family:"Lato",sans-serif}
  .card{position:absolute;top:33px;width:358px;height:834px;background:var(--paper);overflow:hidden}
  .card--front{left:215px}
  .card--back{left:601px}

  /* front */
  .beach-photo{position:absolute;inset:0;
    background:linear-gradient(180deg,var(--sea-deep) 18%,var(--sea-foam) 38%,#e6ddd0 46%,var(--sand-light) 58%,var(--sand-dark) 100%)}
  .logo-disc{position:absolute;left:-95px;top:-320px;width:548px;height:548px;border-radius:50%;
    background:var(--paper);border:1.5px solid var(--rule)}
  .logo{position:absolute;left:50px;top:72px;display:flex;align-items:center;gap:12px}
  .logo__mark{width:34px;height:34px;border-radius:50%;background:var(--ribbon)}
  .logo__name{font-family:"Lato",sans-serif;font-weight:400;color:var(--logo-ink);font-size:25px;line-height:27px;letter-spacing:1px;text-transform:uppercase}
  .award-badge{position:absolute;left:90px;top:211px;width:178px;height:360px}
  .web-bar{position:absolute;left:0;top:798px;width:100%;height:25px;background:var(--ribbon);
    color:#fff;font-weight:300;font-size:16px;text-align:center;line-height:25px}

  /* back */
  .back-wash{position:absolute;left:0;top:134px;width:100%;height:700px;
    background:linear-gradient(180deg,#fff 0%,#eef1f0 18%,#f3efe9 55%,#e9e1d6 100%)}
  .price-list{position:absolute;left:33px;top:60px;width:300px}
  .section__title{font-family:"Crimson Pro",serif;font-weight:400;color:var(--heading);font-size:16px;line-height:19px}
  .section__items{list-style:none;color:var(--ink);font-weight:300;font-size:15px;line-height:19.2px}
  .section__items li{padding-left:13px;text-indent:-9px}
  .section__items li::before{content:"•";display:inline-block;width:9px;text-indent:0}
  .rule{border:0;border-top:1.5px dashed var(--rule);margin:9px -15px 9px -15px}
  .contact{position:absolute;left:0;top:634px;width:100%;height:188px;background:var(--ribbon);
    color:#fff;font-weight:300;font-size:16px;line-height:19.2px;padding:12px 0 0 36px}
  .contact p+p{margin-top:19px}
  .contact__web{position:absolute;left:36px;bottom:8px}
</style>
</head>
<body>
  <section class="card card--front">
    <div class="beach-photo" role="img" aria-label="Beach photo: gentle waves over smooth sand with two hearts drawn in the sand"></div>
    <div class="logo-disc"></div>
    <div class="logo">
      <span class="logo__mark"></span>
      <span class="logo__name">Silver Reel<br>Productions</span>
    </div>
    <svg class="award-badge" viewBox="0 0 178 360" role="img" aria-label="Award ribbon">
      <polygon points="0,0 178,0 178,360 89,336 0,360" fill="var(--ribbon)"/>
    </svg>
    <div class="web-bar">www.srpvowfilms.com</div>
  </section>

  <section class="card card--back">
    <div class="back-wash" role="img" aria-label="Faded beach photo of sand and surf behind the price list"></div>
    <div class="price-list">
      <div class="section">
        <h3 class="section__title">All Packages include:</h3>
        <ul class="section__items">
          <li>Broadcast Quality Equipment shot in HD</li>
          <li>Personalized DVD</li>
          <li>Remote Microphone for clear audio</li>
          <li>Professional editing</li>
        </ul>
      </div>
      <hr class="rule">
      <div class="section">
        <h3 class="section__title">Ceremony Only Coverage – $399</h3>
        <ul class="section__items"><li>Up to 1 hour of coverage.</li></ul>
      </div>
      <hr class="rule">
      <div class="section">
        <h3 class="section__title">Classic Package – $999</h3>
        <ul class="section__items">
          <li>Up to 5 hours of coverage.</li>
          <li>Background music where suitable.</li>
          <li>Names of the bridal party and family.</li>
        </ul>
      </div>
      <hr class="rule">
      <div class="section">
        <h3 class="section__title">Deluxe Package – $1299</h3>
        <ul class="section__items">
          <li>Up to 6 hours of coverage.</li>
          <li>Background music where suitable.</li>
          <li>Names of the bridal party and family.</li>
          <li>An online recap of the wedding highlights edited to your song choice.</li>
          <li>Two extra DVD copies in custom cases.</li>
        </ul>
      </div>
      <hr class="rule">
      <div class="section">
        <h3 class="section__title">Extras</h3>
        <ul class="section__items">
          <li>Hourly Coverage $100/hour</li>
          <li>DVD Copy $25</li>
          <li>Blu Ray Copy $50</li>
          <li>Photo Montage up to 25 photos $150</li>
          <li>Drone Aerial Coverage $250/hour</li>
          <li>Entire Wedding on the Cloud $100</li>
        </ul>
      </div>
    </div>
    <div class="contact">
      <p>Our Millbrook studio is located at:<br>48 Harbor Lane<br>Millbrook, CT 06000</p>
      <p>At the beautiful Maple Ridge Inn Property<br>Oakfield, CT - 555-218-4093<br>Palm Shores, FL - 555-372-6148</p>
      <p class="contact__web">www.srpvowfilms.com</p>
    </div>
  </section>
</body>
</html>
```